Velora Trenn Brochure for Chemicals Products

We need a bifold A3 brochure for the exhibition.
you can visit our company website (www.veloratrenn.example) for more information about our company.
Company logo and color code attached.
The brochure should contain brief introduction of company, industries, product, and contact (address , telephone and email; pavel.k@veloratrenn.example)

Product Portfolio:
1. Intermediates
2. Plastics
3. Rubber
4. Additive
5. Fiber
Detail of each products portfolio are in the website. we would like to add product detail but you may help to design how to put it beautifully.

Target Market(s)

Our customers are factories in related industry.

Industry/Entity Type

Automotive, Paint, Electrical Appliance, Tyre and footwear, Textile, Animal Feed, Lubricant

Font styles to use
Sans Serif

Requirements
Must have
• Logo, Product Portfolio for different market.
Nice to have
• prefer curve design rather than rectangular

```html
<!DOCTYPE html>
<html lang="en">
<head>
<meta charset="utf-8">
<title>Velora Trenn – Product Brochure</title>
<link href="https://fonts.googleapis.com/css2?family=Fira+Sans:wght@400;500;600;700;800&display=swap" rel="stylesheet">
<style>
:root{
  --page:#e3e5e8;
  --blue:#0b8fd9;
  --blue-deep:#1579c9;
  --green:#9cc623;
  --green-deep:#86b21a;
  --ink:#3b3b3b;
  --paper:#ffffff;
  --paper-soft:#eef1f4;
}
*{margin:0;padding:0;box-sizing:border-box}
html,body{width:1200px;height:1070px;overflow:hidden;background:var(--page)}
body{position:relative;font-family:"Fira Sans",Arial,sans-serif;color:var(--ink)}
.spread{position:absolute;width:1150px;height:812px;transform-origin:0 0;transform:scale(.6348);background:var(--paper);box-shadow:0 6px 20px rgba(0,0,0,.18);overflow:hidden}
.spread--outer{left:30px;top:15px}
.spread--inner{left:440px;top:540px}
.spread-bg{position:absolute;inset:0}
.blk{position:absolute}
/* outer spread */
.section-title{font-weight:800;font-size:24px;color:var(--green);letter-spacing:.2px}
.profile-text{width:506px;font-size:11.5px;line-height:14px;color:#fff;text-align:justify;font-weight:500}
.lead-sub{font-size:16px;font-weight:600;color:#fff}
.value-item{width:428px;color:#fff;font-size:11px;line-height:15px;text-align:justify}
.value-item h3{font-size:12px;font-weight:600}
.value-item .single{white-space:nowrap;text-align:left}
.brand-name{font-weight:500;color:var(--blue-deep);letter-spacing:.5px;text-transform:uppercase;white-space:nowrap}
.contact-title{font-size:17px;font-weight:800;color:var(--blue)}
.contact-name{font-size:14px;font-weight:600;color:#222}
.contact-line{font-size:12.5px;line-height:17px;color:#222;display:flex;gap:6px;align-items:flex-start}
.contact-line svg{flex:none;margin-top:3px}
.tagline{font-weight:800;font-size:37px;line-height:41px;letter-spacing:.3px}
.tagline .t-blue{color:var(--blue)}
.tagline .t-green{color:var(--green)}
/* inner spread */
.portfolio-title{font-size:23px;font-weight:800;color:var(--blue)}
.cat-title{font-size:17px;font-weight:800;color:var(--green-deep)}
.intro{font-size:10.5px;line-height:13.5px;text-align:justify;color:#222;letter-spacing:-.1px}
.intro--oneline{white-space:nowrap;text-align:left}
.group-title{font-size:13px;font-weight:500;color:var(--blue);display:flex;align-items:baseline;white-space:nowrap}
.group-title::after{content:"";flex:1;border-bottom:1px dotted var(--blue);margin-left:2px}
.cols{display:flex;gap:10px;margin-top:2px}
.cols ul{list-style:none}
.cols li,.grid-list li{font-size:10.5px;line-height:15.5px;color:#333;white-space:nowrap}
.cols li::before,.grid-list li::before{content:"• "}
.grid-list{display:grid;grid-template-columns:auto auto auto;column-gap:10px;margin-top:2px;list-style:none;justify-content:start}
.grid-list li.blank::before{content:""}
.grid-list li.span2{grid-column:2 / span 2}
.note{font-size:10.5px;line-height:12px;color:#333;white-space:nowrap}
.photo-disc{position:absolute;border-radius:50%;border:6px solid var(--green);box-shadow:0 0 0 3px #fff inset}
</style>
</head>
<body>

<!-- Outer spread: back panel + cover -->
<section class="spread spread--outer">
  <svg class="spread-bg" width="1150" height="812" viewBox="0 0 1150 812" aria-hidden="true">
    <defs>
      <linearGradient id="paperFade" x1="0" y1="0" x2="0" y2="1">
        <stop offset="0" stop-color="#f7f8fa"/><stop offset="1" stop-color="#e9ecef"/>
      </linearGradient>
      <radialGradient id="bandBall" cx=".55" cy=".45" r=".6">
        <stop offset="0" stop-color="#f2f0ec"/><stop offset=".45" stop-color="#e8d9d2"/><stop offset="1" stop-color="#c9c4bc"/>
      </radialGradient>
      <clipPath id="coverClip"><rect x="575" y="0" width="575" height="560"/></clipPath>
    </defs>
    <rect width="1150" height="812" fill="url(#paperFade)"/>
    <path d="M0,0 H1150 V530 C1080,560 1000,600 900,596 C760,590 660,540 560,495 C430,440 230,445 0,478 Z" fill="var(--blue)"/>
    <path d="M0,500 C230,466 430,464 560,517 C660,560 760,612 900,618 C1000,622 1080,588 1150,556" fill="none" stroke="var(--green)" stroke-width="16"/>
    <g clip-path="url(#coverClip)">
      <circle cx="1120" cy="60" r="436" fill="var(--green)"/>
      <circle cx="1120" cy="60" r="422" fill="url(#bandBall)" role="img" aria-label="Photo of a ball of colourful rubber bands on a wooden table"/>
    </g>
    <rect x="574" y="0" width="2" height="812" fill="rgba(0,0,0,.05)"/>
  </svg>

  <h2 class="blk section-title" style="left:34px;top:30px">COMPANY PROFILE:</h2>
  <p class="blk profile-text" style="left:34px;top:58px">Established since 2004, Velora Trenn is a specialties chemicals and polymer distribution company serving customers in various industries, including coating, adhesives, automotive, electrical appliances, construction, medicals, tyre and rubber, animal feed, and textiles. Our products range from chemical intermediates, engineering plastics, synthetics rubber, additives, fiber and our own tailored made products. At Velora Trenn, our dedicated team thrive on providing innovative solutions and unmatched service to customers.</p>

  <h2 class="blk section-title" style="left:34px;top:163px">WHO WE ARE</h2>
  <p class="blk lead-sub" style="left:34px;top:191px">We Create Value In Chemicals Distribution Network</p>
  <p class="blk profile-text" style="left:34px;top:215px">We are deeply dedicated to the long-term growth and success of our partners and our people. We are dedicated to producing measured value and results.</p>

  <svg class="blk" style="left:36px;top:252px" width="54" height="170" aria-hidden="true">
    <g fill="none" stroke="var(--green)" stroke-width="2">
      <circle cx="27" cy="25" r="24" fill="rgba(156,198,35,.25)"/>
      <circle cx="27" cy="82" r="24" fill="rgba(156,198,35,.25)"/>
      <circle cx="27" cy="141" r="24" fill="rgba(156,198,35,.25)"/>
    </g>
  </svg>
  <div class="blk value-item" style="left:112px;top:254px"><h3>Business &amp; Market Strategy</h3><p>Develop and promote new product from suppliers globally. Bring benefit to our clients through our network and expertise. Deliver what customer's needs.</p></div>
  <div class="blk value-item" style="left:112px;top:311px"><h3>Excellence In Services</h3><p>Beyond logistics provider. When you get one of us, you get all of us. We bring innovative solutions and reliable advice.</p></div>
  <div class="blk value-item" style="left:112px;top:376px"><h3>Our People Make Difference</h3><p class="single">Well committed and qualified with years of experience team. We serve you with our</p></div>

  <div class="photo-disc" style="left:320px;top:421px;width:216px;height:216px;background:radial-gradient(circle at 55% 45%,#cfe4fb,#5f9ddf 55%,#1d4f9f)" role="img" aria-label="Photo of a laboratory pipette dropping liquid into glassware"></div>

  <div class="blk brand-name" style="left:34px;top:598px;font-size:27px">Velora Trenn</div>

  <h3 class="blk contact-title" style="left:34px;top:697px">CONTACT US</h3>
  <p class="blk contact-name" style="left:34px;top:723px">PAVEL KORSGAARD</p>
  <div class="blk contact-line" style="left:34px;top:745px">
    <svg width="12" height="12" viewBox="0 0 12 12"><circle cx="6" cy="6" r="6" fill="var(--blue)"/><path d="M3,6.5 6,3.5 9,6.5 V9 H3Z" fill="#fff"/></svg>
    <span>18/4 Maple Lane 7, Riverside Rd.,<br>Harbour, Bangrak, Bangkok 10500 Thailand</span>
  </div>
  <div class="blk contact-line" style="left:330px;top:721px">
    <svg width="12" height="12" viewBox="0 0 12 12"><circle cx="6" cy="6" r="5.3" fill="none" stroke="var(--blue)" stroke-width="1.4"/><path d="M4,3.5 5.2,4.7 4.6,5.5 6.5,7.4 7.3,6.8 8.5,8 7.5,9 C5.5,9 3,6.5 3,4.5Z" fill="var(--blue)"/></svg>
    <span>+66-81-555-0142</span>
  </div>
  <div class="blk contact-line" style="left:330px;top:741px">
    <svg width="12" height="12" viewBox="0 0 12 12"><circle cx="6" cy="6" r="5.3" fill="none" stroke="var(--blue)" stroke-width="1.4"/><rect x="3.3" y="4.2" width="5.4" height="3.8" fill="none" stroke="var(--blue)" stroke-width="1"/></svg>
    <span>pavel.k@veloratrenn.example</span>
  </div>
  <div class="blk contact-line" style="left:330px;top:760px">
    <svg width="12" height="12" viewBox="0 0 12 12"><circle cx="6" cy="6" r="5.3" fill="none" stroke="var(--blue)" stroke-width="1.4"/><circle cx="6" cy="6" r="2.6" fill="var(--blue)"/></svg>
    <span>www.veloratrenn.example</span>
  </div>

  <div class="blk" style="left:887px;top:418px;width:224px;height:224px;border-radius:50%;background:#fff;border:4px solid var(--blue);display:flex;align-items:center;justify-content:center">
    <span class="brand-name" style="font-size:25px">Velora Trenn</span>
  </div>

  <div class="blk tagline" style="left:621px;top:652px">
    <div class="t-blue">THE BEST VALUE</div>
    <div class="t-green">FOR BUSINESS</div>
    <div class="t-blue">WITH PERFECT GROWTH</div>
  </div>
</section>

<!-- Inner spread: product portfolio -->
<section class="spread spread--inner">
  <svg class="spread-bg" width="1150" height="812" viewBox="0 0 1150 812" aria-hidden="true">
    <rect width="1150" height="812" fill="#fff"/>
    <rect x="575" width="575" height="812" fill="#fbfcfd"/>
    <path d="M960,0 C1040,2 1080,30 1110,80 L1150,80 V0 Z" fill="var(--green)"/>
    <path d="M1030,0 C1100,14 1128,50 1128,110 V700 L1150,700 V0 Z" fill="var(--blue)"/>
    <path d="M820,812 C930,800 1050,780 1150,730 V812 Z" fill="var(--green)"/>
    <path d="M900,812 C990,800 1080,770 1150,690 V812 Z" fill="var(--blue)"/>
    <rect x="574" y="0" width="2" height="812" fill="rgba(0,0,0,.05)"/>
  </svg>

  <!-- Left page -->
  <h2 class="blk portfolio-title" style="left:34px;top:30px">OUR PRODUCT PORTFOLIO</h2>
  <p class="blk intro" style="left:34px;top:56px;width:472px;font-weight:500">From upstream to downstream, our portfolio covers various polymer related products including customs formulation solutions</p>

  <h3 class="blk cat-title" style="left:34px;top:92px">CHEMICALS &amp; INTERMEDIATES</h3>
  <p class="blk intro" style="left:34px;top:112px;width:472px">Our chemicals range from intermediates, monomer, and other products bringing synergy to our client. We offer products to coating resin, ink, adhesive, polyurethane, lubricants, polymer polymerization, textile auxiliaries, etc.</p>

  <div class="blk" style="left:34px;top:160px;width:330px">
    <div class="group-title">Intermediates and Monomer</div>
    <div class="cols">
      <ul><li>Oxalic Acid</li><li>Malic Acid</li><li>Adipic Acid</li><li>Acrylic Acid</li></ul>
      <ul><li>Bio MEG</li><li>Bio DEG</li><li>iBMA</li><li>PTMEG</li></ul>
      <ul><li>MMA</li><li>MAA</li><li>nBMA</li><li>DMF</li></ul>
      <ul><li>BDO</li><li>NPG</li><li>MDI</li><li>THF</li></ul>
      <ul><li>Bio Succinic Acid</li><li style="line-height:11px">Hexamethylene<br>&nbsp;&nbsp;&nbsp;Diamine</li></ul>
    </div>
  </div>
  <div class="blk" style="left:34px;top:252px;width:120px">
    <div class="group-title">Other Chemicals</div>
    <div class="cols"><ul><li>Silicone Hard Coat</li><li>Phenoxy Resin</li><li>Acrylic Resin</li><li>Caprolactone</li></ul></div>
  </div>
  <div class="blk" style="left:175px;top:252px;width:180px">
    <div class="group-title">Oil &amp; Plasticizers</div>
    <ul class="grid-list">
      <li>DINP</li><li>DOS</li><li>Paraffinic Oil</li>
      <li>DIDP</li><li>ESBO</li><li>Naphthenic Oil</li>
      <li>DOA</li><li>Bio Oil</li><li class="blank"></li>
      <li>DOTP</li><li class="span2">Biomass Plasticizer</li>
    </ul>
  </div>
  <div class="photo-disc" style="left:366px;top:160px;width:174px;height:174px;background:conic-gradient(#e0328a,#f4d31f,#2fb7e8,#6b3bc8,#e23a3a,#e0328a)" role="img" aria-label="Photo of open paint cans in bright colours"></div>

  <h3 class="blk cat-title" style="left:34px;top:370px">RUBBER</h3>
  <p class="blk intro intro--oneline" style="left:34px;top:390px">We supply synthetic rubber to major tire producers as well as rubber compounder and converter.</p>
  <div class="blk" style="left:34px;top:410px;width:300px">
    <div class="group-title">Synthetic Rubber</div>
    <div class="cols">
      <ul><li>SBR</li><li>SSBR</li></ul><ul><li>BR</li><li>EPDM</li></ul><ul><li>CIIR</li><li>NBR</li></ul><ul><li>IIR</li><li>BIIR</li></ul><ul><li>HNBR</li><li>IR</li></ul><ul><li>NBR/PVC</li></ul>
    </div>
  </div>
  <div class="blk" style="left:34px;top:465px;width:180px">
    <div class="group-title">Antioxidant</div>
    <div class="cols"><ul><li>Phenolic Antioxidant (BHT, SPH, BPH)</li><li>Amine Antioxidant (6PPD, IPPD, TMQ)</li><li>Secondary Antioxidant (TNPP)</li></ul></div>
  </div>
  <div class="blk" style="left:228px;top:465px">
    <div class="group-title">Rubber Compound</div>
    <div class="cols"><ul><li>FKM</li></ul></div>
    <div class="group-title" style="margin-top:2px">Latex</div>
    <div class="cols"><ul><li>NB Latex</li></ul></div>
  </div>
  <div class="blk" style="left:34px;top:538px;width:180px">
    <div class="group-title">Filler</div>
    <div class="cols"><ul><li>Silica (Micro Pearl, Powder, Granule)</li><li>Silane Coupling Agent (Si69, Si75)</li><li>China Clay, Kaolin Clay</li><li>Barium Sulfate</li><li>Talc</li><li>Wollastonite</li></ul></div>
  </div>
  <div class="blk" style="left:228px;top:538px">
    <div class="group-title">Activator &amp; Retarder</div>
    <div class="cols"><ul><li>Zinc Oxide</li><li>PVI</li></ul><ul><li>Stearic Acid</li><li>Salicylic Acid</li></ul></div>
  </div>
  <div class="blk" style="left:228px;top:597px;width:312px">
    <div class="group-title">Process Oil and Plasticizer</div>
    <div class="cols"><ul><li>Paraffinic Oil</li><li>Naphthenic Oil</li><li>Bio Based Oil</li></ul><ul><li>Mineral White Oil</li><li>Bio Based Plasticizer</li><li>Non Phthalate Plasticizer (DOA, DOS, DOTP)</li></ul></div>
  </div>
  <div class="photo-disc" style="left:366px;top:416px;width:174px;height:174px;background:radial-gradient(circle at 60% 40%,#f6b9d4,#c8dcef 45%,#eef1f4 75%)" role="img" aria-label="Photo of a ball of colourful rubber bands"></div>

  <div class="blk" style="left:34px;top:669px;width:368px">
    <div class="group-title">Vulcanising Agent &amp; Accelerator</div>
    <div class="cols"><ul><li>Insoluble Sulfur</li><li>Primary Accelerator - Thiazole (MBT, MBTS, ZMBT)</li><li>Primary Accelerator - Sulphenamide Accelerator (CBS, TBBS, MBS, DCBS)</li><li>Secondary Accelerator - Guanidine (DPG, DOTG)</li><li>Secondary Accelerator - Thiuram Accelartor (TMTD, TMTM, TETD, MPTD)</li><li>Secondary Accelerator - Dithiocarbamate Accelerator (ZDEC, ZDMC, ZDBC)</li></ul></div>
  </div>
  <div class="blk" style="left:430px;top:678px;width:110px">
    <div class="group-title">Wax</div>
    <div class="cols"><ul><li>PE Wax</li><li>Oxidized Wax</li><li>Anti Ozonant Wax</li><li>Micro Crystalline Wax</li></ul></div>
  </div>

  <!-- Right page -->
  <h3 class="blk cat-title" style="left:608px;top:30px">PLASTICS</h3>
  <p class="blk intro" style="left:608px;top:50px;width:515px;text-align:left">We offer polymer &amp; compound materials including short glass fiber, long glass fiber, mineral fillers, conductive, flame retardant, magnetic compound, carbon fiber, color compound &amp; other customs compound.</p>
  <div class="blk" style="left:608px;top:90px;width:125px">
    <div class="group-title">Standard Polymer</div>
    <div class="cols"><ul><li>PE</li><li>PP</li></ul><ul><li>PS</li><li>SAN</li></ul><ul><li>PVC</li><li>EVA</li></ul></div>
  </div>
  <div class="blk" style="left:744px;top:90px;width:185px">
    <div class="group-title">Elastomer</div>
    <div class="cols"><ul><li>SBS</li><li>SEBS</li></ul><ul><li>TPE</li><li>TPV</li></ul><ul><li>TPU</li><li>TPEE</li></ul><ul><li>POE</li></ul></div>
  </div>
  <div class="blk" style="left:608px;top:148px;width:212px">
    <div class="group-title">Engineering Plastics</div>
    <div class="cols"><ul><li>ABS</li><li>ASA</li><li>PC</li></ul><ul><li>POM</li><li>PETG</li><li>PMMA</li></ul><ul><li>PBT</li><li>PET</li><li>PA6</li></ul><ul><li>PC/ABS</li><li>PA66</li><li>PA610</li></ul><ul><li>PA12</li><li>PPA</li><li>PPE</li></ul></div>
  </div>
  <div class="blk" style="left:835px;top:148px;width:100px">
    <div class="group-title">Polyurethanes</div>
    <div class="cols"><ul><li>Polyester Polyol</li><li>Polyether Polyol</li><li>PU System</li></ul></div>
  </div>
  <div class="blk" style="left:608px;top:220px;width:185px">
    <div class="group-title">Specialties Polymer</div>
    <div class="cols"><ul><li>PPS</li><li>PPSU</li><li>PESU</li></ul><ul><li>PVDF</li><li>PEEK</li><li>PAEK</li></ul><ul><li>PARA</li><li>PAI</li><li>PFPE</li></ul><ul><li>ECTFE</li></ul></div>
  </div>
  <div class="blk" style="left:835px;top:224px;width:100px">
    <div class="group-title">Green Polymer</div>
    <div class="cols"><ul><li>PLA</li><li>PHA</li><li>PBS</li></ul><ul><li>PBAT</li><li>PCR Material</li><li>PIR Material</li></ul></div>
  </div>
  <div class="photo-disc" style="left:940px;top:96px;width:168px;height:168px;background:radial-gradient(circle at 40% 55%,#e9b8a0,#7fc6de 40%,#a7dcec)" role="img" aria-label="Photo of a hand holding blue plastic pellets"></div>

  <h3 class="blk cat-title" style="left:608px;top:313px">ADDITIVES</h3>
  <p class="blk intro" style="left:608px;top:331px;width:515px;text-align:left">We provide wide product range of additives for plastics compound, rubber compound, coating, modified starch and animal feed. We also offer additive masterbatch used for packaging industries.</p>
  <div class="blk" style="left:608px;top:361px;width:310px">
    <div class="group-title">Additives</div>
    <div class="cols"><ul><li>PE Wax</li><li>Antistatic</li><li>Antifog</li><li>Antioxidants</li></ul><ul><li>Antiozone Wax</li><li>Blowing Agent</li><li>Mold Release</li><li>Insoluble Sulfur</li></ul><ul><li>Micro Crystalline Wax</li><li>Rubber Accelerator</li><li>UV Absorber &amp; UV Stabilizer</li></ul></div>
  </div>
  <div class="blk" style="left:608px;top:444px;width:310px">
    <div class="group-title">Oil &amp; Plasticizers</div>
    <div class="cols"><ul><li>Paraffinic Oil</li><li>Naphthenic Oil</li></ul><ul><li>Bio Oil</li><li>DINP</li></ul><ul><li>DIDP</li><li>DOA</li></ul><ul><li>DOTP</li><li>DOS</li></ul><ul><li>ESBO</li><li>Biomass Plasticizer</li></ul></div>
  </div>
  <div class="blk" style="left:608px;top:500px;width:250px">
    <div class="group-title">Additive Masterbatches</div>
    <div class="cols"><ul><li>Filler Masterbatch</li><li>Color Masterbatch</li><li>Cleaning Agent</li></ul><ul><li>Slip &amp; Antiblock Masterbatch</li><li>Processing Aid Masterbatch</li></ul></div>
  </div>
  <div class="blk" style="left:871px;top:500px;width:66px">
    <div class="group-title">Fillers</div>
    <div class="cols"><ul><li>Silica</li><li>Mineral Fillers</li></ul></div>
    <p class="note">(Talc, Mica, Kaolin, Barium Sulfate, Wollastonite)</p>
  </div>
  <div class="photo-disc" style="left:940px;top:352px;width:168px;height:168px;background:radial-gradient(circle at 45% 60%,#f1f3f4,#c9dde6 45%,#7fb4c9)" role="img" aria-label="Photo of a lab worker pouring liquid into a bowl"></div>

  <h3 class="blk cat-title" style="left:608px;top:598px">FIBERS</h3>
  <p class="blk intro" style="left:608px;top:616px;width:325px;text-align:left">We offer specialties staple fiber &amp; filament yarn for nonwoven, textile spinning, flooring, abrasives, tire cord, and protection fabric. The functionalized products such as antibacteria, flame retardant, biodegradable fiber are also available.</p>
  <div class="blk" style="left:608px;top:673px;width:145px">
    <div class="group-title">Staple Fiber</div>
    <div class="cols"><ul><li>PA bonding fiber</li><li>Meta aramid</li><li>Aramid pulp</li></ul><ul><li>PA6</li><li>PA66</li></ul></div>
  </div>
  <div class="blk" style="left:790px;top:673px;width:115px">
    <div class="group-title">Filament Yarn</div>
    <div class="cols"><ul><li>PA high tenacity yarn</li><li>Fusible bonded yarn</li><li>PA BCF yarn</li><li>Flock Tow</li></ul></div>
  </div>
  <div class="photo-disc" style="left:940px;top:598px;width:168px;height:168px;background:radial-gradient(circle at 50% 45%,#6aa0e6,#2a5fb8 55%,#143b82)" role="img" aria-label="Photo of blue yarn spools"></div>
</section>

</body>
</html>
```